Rolla Maki Hospitality Brochure for Industry leaders within the catering space

We need a brochure created for a Sushi franchise called Rolla Maki. The brochure will be 6 pages including the front and back pages.
Background white.
Content to be displayed as written.
Images to be creatively placed throughout document.

refer to www.rollamaki.com.au

refer to document notes

Target Market(s)

hospitality catering companies
remote locations

Font styles to use
Other font styles liked:
• some wood finish is ok.

Colors
ec1f27
ffffff

Requirements
Must have
• stylish
A4
Portrait
Nice to have
• background photos included
health
well being

```html
<!DOCTYPE html>
<html lang="en">
<head>
<meta charset="utf-8">
<title>Rolla Maki – Hospitality Brochure</title>
<link rel="stylesheet" href="https://fonts.googleapis.com/css2?family=Montserrat:wght@300;400;600;700;800;900&family=Open+Sans:wght@400;600&display=swap">
<style>
  :root{
    --red:#ec1f27;
    --red-deep:#c8222a;
    --white:#ffffff;
    --ink:#2a2a2a;
    --text:#444444;
    --stage:#b9b9b9;
    --paper-shade:#f4f4f4;
    --green:#3a9a4a;
  }
  *{box-sizing:border-box;margin:0;padding:0}
  html,body{width:1200px;height:2707px;overflow:hidden}
  body{background:var(--stage);font-family:"Open Sans",Arial,sans-serif;color:var(--text);position:relative}

  .page{position:absolute;background:var(--white);overflow:hidden;box-shadow:0 6px 18px rgba(0,0,0,.18)}

  /* brand name block */
  .brand{display:flex;align-items:center;gap:8px;font-family:"Montserrat",Arial,sans-serif;font-weight:800;color:var(--red);white-space:nowrap}
  .brand-dot{border-radius:50%;background:var(--red);flex:none}

  /* cover */
  .cover{width:500px;height:707px}
  .cover .brand{position:absolute;top:86px;right:56px;font-size:38px}
  .cover .brand-dot{width:16px;height:16px}
  .cover-photo{position:absolute;top:180px;left:140px;width:300px;height:270px;border-radius:14px;
    background:radial-gradient(circle at 60% 25%,#f08a4b 0 22%,transparent 40%),linear-gradient(160deg,#f3a46f 0%,#d9c6a8 40%,#2f3a2c 75%,#1f261d 100%)}
  .cover-title{position:absolute;left:40px;top:480px;font-family:"Montserrat",Arial,sans-serif;line-height:1}
  .cover-title .light{display:block;font-weight:300;font-size:46px;color:var(--ink);letter-spacing:1px}
  .cover-title .bold{display:block;font-weight:900;font-size:44px;color:var(--red);margin-top:6px}
  .cover-url{position:absolute;left:40px;top:600px;font-family:"Montserrat",Arial,sans-serif;font-weight:700;font-size:21px;color:var(--ink);letter-spacing:.5px}
  .edge-band{position:absolute;left:0;right:0;bottom:0;height:9px;background:var(--red)}

  /* back cover */
  .back-photo{position:absolute;top:0;left:120px;width:380px;height:330px;
    background:radial-gradient(ellipse at 55% 40%,rgba(240,170,120,.45),rgba(255,255,255,0) 70%);}
  .back .brand{position:absolute;left:40px;top:560px;font-size:24px}
  .back .brand-dot{width:11px;height:11px}
  .contact{position:absolute;top:545px;font-family:"Montserrat",Arial,sans-serif;font-size:10px;color:var(--ink);line-height:1.55}
  .contact-franchise{left:210px}
  .contact-general{left:345px;padding-left:14px;border-left:1px solid #999}
  .contact-swatch{width:18px;height:12px;margin-bottom:5px}
  .contact-swatch.red{background:var(--red)}
  .contact-swatch.black{background:#111}
  .contact h4{font-size:11px;font-weight:700}
  .contact-line{display:flex;align-items:center;gap:5px}
  .contact-line svg{flex:none}
  .social{display:flex;gap:6px;margin-top:5px}
  .social span{width:10px;height:10px;border-radius:50%;background:var(--red)}

  /* inside spread */
  .inside{width:440px;height:640px}
  .inside-band{height:78px;background:linear-gradient(90deg,var(--red-deep),var(--red));color:var(--white);font-family:"Montserrat",Arial,sans-serif;display:flex;flex-direction:column;justify-content:center}
  .inside-left .inside-band{padding-left:50px;font-size:19px;font-weight:400}
  .inside-left .inside-band b{font-weight:800}
  .inside-right .inside-band{padding-left:44px;font-size:17px;line-height:1.2;font-weight:400}
  .inside-right .inside-band b{font-weight:800;display:block}
  .inside-photo{position:absolute;background:linear-gradient(135deg,#7a5a3e 0%,#c2492e 45%,#3c3c3c 100%)}
  .inside-left .inside-photo{left:42px;top:92px;width:356px;height:222px}
  .inside-body{position:absolute;left:42px;top:334px;width:350px;font-size:10.5px;line-height:1.35}
  .inside-body p{margin-bottom:12px}
  .inside-foot{position:absolute;left:42px;right:42px;bottom:40px;display:flex;align-items:center;gap:14px}
  .inside-foot .brand{font-size:15px}
  .inside-foot .brand-dot{width:8px;height:8px}
  .inside-foot .rule{flex:1;height:1px;background:#777}
  .inside-foot .url{font-family:"Montserrat",Arial,sans-serif;font-weight:600;font-size:10.5px;color:var(--ink)}

  .inside-right h3{position:absolute;left:44px;top:88px;width:360px;font-family:"Montserrat",Arial,sans-serif;font-weight:700;font-size:16px;color:var(--ink);line-height:1.25}
  .points{position:absolute;left:44px;top:140px;width:370px;list-style:none}
  .points li{display:flex;gap:14px;margin-bottom:12px;font-size:10px;line-height:1.3}
  .points .num{flex:none;width:34px;height:34px;border-radius:50%;background:var(--green);color:var(--white);font-family:"Montserrat",Arial,sans-serif;font-weight:800;font-size:15px;display:flex;align-items:center;justify-content:center}
  .inside-right .inside-photo{left:0;right:0;bottom:0;height:220px;background:linear-gradient(180deg,#f0ece6 0%,#d8c7a8 35%,#5b5b55 80%,#2b2b2b 100%)}
</style>
</head>
<body>

  <!-- front cover -->
  <section class="page cover" style="left:350px;top:96px">
    <div class="brand"><span class="brand-dot"></span>Rolla Maki</div>
    <div class="cover-photo" role="img" aria-label="Photo of salmon and sesame sushi rolls stacked together"></div>
    <h1 class="cover-title"><span class="light">MORE CHOICE</span><span class="bold">AT MEALTIMES!</span></h1>
    <div class="cover-url">www.rollamaki.com.au</div>
    <div class="edge-band"></div>
  </section>

  <!-- back and front cover spread -->
  <section class="page cover back" style="left:100px;top:930px">
    <div class="back-photo" role="img" aria-label="Faded photo of assorted sushi pieces scattered across the top of the page"></div>
    <div class="brand"><span class="brand-dot"></span>Rolla Maki</div>
    <div class="contact contact-franchise">
      <div class="contact-swatch red"></div>
      <h4>Franchising</h4>
      <div class="contact-line"><svg width="8" height="8" viewBox="0 0 10 10"><path d="M2 1l2 2-1 1.5a6 6 0 0 0 2.5 2.5L7 6l2 2-1.5 1.5C4.5 9 1 5.5.5 2.5z" fill="#ec1f27"/></svg>(02) 5550 0142</div>
      <div class="contact-line"><svg width="8" height="8" viewBox="0 0 10 10"><circle cx="5" cy="5" r="4" fill="#ec1f27"/></svg>rollamaki.com.au</div>
      <div class="social"><span></span><span></span><span></span></div>
    </div>
    <div class="contact contact-general">
      <div class="contact-swatch black"></div>
      <h4>General</h4>
      <div class="contact-line"><svg width="8" height="8" viewBox="0 0 10 10"><path d="M2 1l2 2-1 1.5a6 6 0 0 0 2.5 2.5L7 6l2 2-1.5 1.5C4.5 9 1 5.5.5 2.5z" fill="#ec1f27"/></svg>(02) 5550 0142</div>
      <div class="contact-line"><svg width="8" height="10" viewBox="0 0 10 12"><path d="M5 0a4 4 0 0 1 4 4c0 3-4 8-4 8S1 7 1 4a4 4 0 0 1 4-4z" fill="#ec1f27"/></svg>PO Box 410</div>
      <div>Kirribilli NSW 2061</div>
      <div>Australia</div>
      <div class="contact-line"><svg width="8" height="8" viewBox="0 0 10 10"><circle cx="5" cy="5" r="4" fill="#ec1f27"/></svg>rollamaki.com.au</div>
    </div>
    <div class="edge-band"></div>
  </section>
  <section class="page cover" style="left:600px;top:930px">
    <div class="brand"><span class="brand-dot"></span>Rolla Maki</div>
    <div class="cover-photo" role="img" aria-label="Photo of salmon and sesame sushi rolls stacked together"></div>
    <h1 class="cover-title"><span class="light">MORE CHOICE</span><span class="bold">AT MEALTIMES!</span></h1>
    <div class="cover-url">www.rollamaki.com.au</div>
    <div class="edge-band"></div>
  </section>

  <!-- inside spread -->
  <section class="page inside inside-left" style="left:160px;top:1930px">
    <div class="inside-band"><div><b>MORE CHOICE</b> AT MEALTIMES!</div></div>
    <div class="inside-photo" role="img" aria-label="Photo from above of friends sharing sushi at a table and taking phone pictures"></div>
    <div class="inside-body">
      <p>We understand how important mealtimes are after such long, hard shifts. Away from home and family, food becomes one of the most appreciated creature comforts for remote workers. So why not provide them with greater variety at a time they need it most – whilst unwinding and socialising?</p>
      <p>Refueling the body with diverse nutrient rich foods is essential in keeping them safe and mentally supported, protecting them from illness and strengthening overall productivity.</p>
      <p>Rolla Maki ticks all the boxes! It's a popular nutritional must-have your workforce will love at any time of the day and with a foolproof franchising system designed for success, the benefits to all are hard to ignore.</p>
    </div>
    <div class="inside-foot">
      <div class="brand"><span class="brand-dot"></span>Rolla Maki</div>
      <div class="rule"></div>
      <div class="url">rollamaki.com.au</div>
    </div>
  </section>
  <section class="page inside inside-right" style="left:600px;top:1930px">
    <div class="inside-band"><div><b>SPICE UP MEALTIMES</b>WITH AN ON-TREND FAVOURITE.</div></div>
    <h3>On trend and loved by more Australians every year!</h3>
    <ul class="points">
      <li><span class="num">01</span><span>Sushi is hugely popular with over 8.5 million Australians ranking it as a favourite meal. According to leading market research organization Hartwell Research, its popularity continues to rise year on year.</span></li>
      <li><span class="num">02</span><span>It offers a powerhouse of nutrition by containing a variety of fish which are full of essential fatty acids for heart and cholesterol health, arterial strength, brain function and importantly to help as a mood-enhancer to alleviate depression (OR to support mental wellbeing).</span></li>
      <li><span class="num">03</span><span>With its fresh colours and creative presentation, sushi celebrates the notion that when you "eat with your eyes" the food becomes more appetizing and enjoyable; a sensory experience that few foods can match.</span></li>
      <li><span class="num">04</span><span>Sushi is a healthy and convenient food choice that workers can grab and go.</span></li>
    </ul>
    <div class="inside-photo" role="img" aria-label="Close-up photo of sushi rolls with pickled ginger on a dark slate board"></div>
  </section>

</body>
</html>
```